Very Simple/Minimal Business Card Design Project

The company operates in the industrial maritime infrastructure sector in Brazil. You can find more information on our website www.navelquor.com.br WE NEED TO LOOK POWERFUL AND SERIOUS
I have attached a copy of the old cards. We would like something more professional / industrial / sexy that also includes the position.

The card can be double sided or not. We would like you to propose as many options.

Thank you
Updates

Many thanks, do let me know if you have any questions. I am under a lot of time pressure to try and have them printed over the next days or so.

Please could you use the following information

for the address: Rua Tapiraçu, 418 - Centro, Rio de Janeiro, 20135-070, Brasil

for the mobile: +55 21 8372 9041
for the landline: +55 21 4067 3859

and position:  Diretor Geral

Thakn you

Target Market(s)

Shipowners, bankers, industrial companies

Industry/Entity Type

Industrial

Requirements
Must have
• POWERFUL
SERIOUS
SOLID
BIG CORPORATION

```html
<!DOCTYPE html>
<html lang="pt-BR">
<head>
<meta charset="utf-8">
<title>Navelquor – Cartão de visita</title>
<link href="https://fonts.googleapis.com/css2?family=Arimo:wght@700&display=swap" rel="stylesheet">
<style>
  :root {
    --navy: #232b6b;
    --green: #1f9a47;
    --paper: #ffffff;
    --backdrop: #e4e5e8;
    --shadow: rgba(20, 24, 40, 0.18);
  }
  * { margin: 0; padding: 0; box-sizing: border-box; }
  html, body { width: 1200px; height: 900px; overflow: hidden; }
  body {
    background: var(--backdrop);
    font-family: "Arimo", Arial, sans-serif;
    font-weight: 700;
    position: relative;
  }
  .card {
    position: absolute;
    left: 270px;
    width: 660px;
    height: 377px;
    background: var(--paper);
    box-shadow: 0 10px 30px var(--shadow);
  }
  .card--back { top: 50px; }
  .card--front { top: 470px; }

  .brand__square { display: block; width: 52px; height: 52px; background: var(--green); border-radius: 6px; }
  .brand__name { color: var(--navy); font-size: 46px; letter-spacing: 0.5px; line-height: 1; }

  .card--back .brand-stack {
    position: absolute; left: 0; right: 0; top: 96px;
    display: flex; flex-direction: column; align-items: center;
  }
  .card--back .brand__square { width: 70px; height: 56px; margin-bottom: 16px; }
  .card--back .brand__name { font-size: 50px; }
  .card--back .website { color: var(--green); font-size: 19px; margin-top: 12px; }

  .card--front .brand {
    position: absolute; left: 56px; top: 62px;
    display: flex; align-items: center; gap: 12px;
  }
  .card--front .brand__name { font-size: 40px; }

  .person { position: absolute; left: 56px; top: 168px; }
  .person__name { color: var(--green); font-size: 24px; letter-spacing: 0.5px; }
  .person__role { color: var(--navy); font-size: 16px; margin-top: 2px; }

  .contacts { position: absolute; left: 56px; top: 236px; list-style: none; }
  .contacts li {
    display: flex; align-items: center; gap: 10px;
    color: var(--navy); font-size: 17px; line-height: 25px;
  }
  .contacts svg { width: 15px; height: 15px; fill: var(--green); flex: none; }

  .address {
    position: absolute; left: 400px; top: 176px;
    font-style: normal; color: var(--navy); font-size: 17px; line-height: 25px;
  }
</style>
</head>
<body>
  <section class="card card--back" aria-label="Verso do cartão">
    <div class="brand-stack">
      <span class="brand__square"></span>
      <span class="brand__name">NAVELQUOR</span>
      <p class="website">www.navelquor.com.br</p>
    </div>
  </section>

  <section class="card card--front" aria-label="Frente do cartão">
    <div class="brand">
      <span class="brand__square"></span>
      <span class="brand__name">NAVELQUOR</span>
    </div>

    <div class="person">
      <p class="person__name">RAFAEL MONTEIRO</p>
      <p class="person__role">Diretor Geral</p>
    </div>

    <ul class="contacts">
      <li>
        <svg viewBox="0 0 16 16" aria-hidden="true"><path d="M3.6 1.2l2.3 2.6-1.2 1.8c.9 2 2.5 3.6 4.5 4.5l1.8-1.2 2.6 2.3-1.4 2.6C6.6 13.4 2.6 9.4 1.2 3z"/></svg>
        + 55 21 4067 3859
      </li>
      <li>
        <svg viewBox="0 0 16 16" aria-hidden="true"><path d="M4.5 0h7A1.5 1.5 0 0 1 13 1.5v13a1.5 1.5 0 0 1-1.5 1.5h-7A1.5 1.5 0 0 1 3 14.5v-13A1.5 1.5 0 0 1 4.5 0zM5 2v10h6V2zm3 11a1 1 0 1 0 0 2 1 1 0 0 0 0-2z"/></svg>
        + 55 21 8372 9041
      </li>
      <li>
        <svg viewBox="0 0 16 16" aria-hidden="true"><path d="M0 3h16v10H0zm1.5 1.4v.3L8 9l6.5-4.3v-.3zM1.5 6.5V11.5h13V6.5L8 10.8z"/></svg>
        rafael@navelquor.com.br
      </li>
      <li>
        <svg viewBox="0 0 16 16" aria-hidden="true"><path d="M8 0a8 8 0 1 0 0 16A8 8 0 0 0 8 0zm0 1.5c.9 0 1.9 1.6 2.3 4H5.7C6.1 3.1 7.1 1.5 8 1.5zM1.7 7h3.8a14 14 0 0 0 0 2H1.7a6.5 6.5 0 0 1 0-2zm5.3 0h2a13 13 0 0 1 0 2H7a13 13 0 0 1 0-2zm3.5 0h3.8a6.5 6.5 0 0 1 0 2h-3.8a14 14 0 0 0 0-2zM5.7 10.5h4.6c-.4 2.4-1.4 4-2.3 4s-1.9-1.6-2.3-4z"/></svg>
        www.navelquor.com.br
      </li>
    </ul>

    <address class="address">
      Rua Tapiraçu, 418<br>
      Centro<br>
      CEP 20135-070<br>
      Rio de Janeiro
    </address>
  </section>
</body>
</html>
```